Harbourline Refrigeration business card design

We would like a new design for our business card as we have a new logo.
We need generic business card to give our customers with our office details - with the option of making it individualized for each manager

Target Market(s)

Companies and homeowners

Industry/Entity Type

Air Conditioning

Contact Information for Business Card

We are not sure if we want single or double sided it will depend on the design we choose

Colors
33a6d7
0255a3

Requirements
Must have
• Logo
• phone: (08) 8721 5940
• email: harbourserve@tealnet.example
• website: www.harbourlinerefrigeration.example
• AU61420
• BLD472913
Nice to have
• Address - Shed 5/284 Tallis Rd, Carrick Vale Brennan SA 5790

```html
<!DOCTYPE html>
<html lang="en">
<head>
<meta charset="utf-8">
<title>Harbourline Refrigeration – Business Card</title>
<link rel="stylesheet" href="https://fonts.googleapis.com/css2?family=Poppins:wght@400;500;600;800&display=swap">
<style>
  :root {
    --backdrop: #4a4948;
    --navy: #173a6e;
    --brand-blue: #0255a3;
    --sky: #33a6d7;
    --ink: #1e1e22;
    --paper: #ffffff;
    --paper-shade: #ececec;
  }
  * { box-sizing: border-box; margin: 0; padding: 0; }
  html, body { width: 1200px; height: 1200px; overflow: hidden; }
  body {
    background: var(--backdrop);
    font-family: "Poppins", sans-serif;
    display: flex;
    flex-direction: column;
    align-items: center;
    justify-content: center;
    gap: 56px;
  }
  .card {
    width: 900px;
    height: 514px;
    position: relative;
    box-shadow: 0 10px 30px rgba(0,0,0,.35);
  }
  .brand {
    display: flex;
    align-items: center;
    gap: 18px;
    font-weight: 600;
    letter-spacing: .5px;
    white-space: nowrap;
  }
  .brand__dot {
    flex: none;
    width: 34px; height: 34px; border-radius: 50%;
  }

  /* Front */
  .card--front {
    background: var(--navy);
    color: var(--paper);
    display: flex;
    flex-direction: column;
    align-items: center;
    justify-content: center;
  }
  .card--front .brand { font-size: 44px; color: var(--paper); }
  .card--front .brand__dot { background: var(--paper); }
  .licence-rule {
    width: 300px; height: 1px;
    background: rgba(255,255,255,.35);
    margin: 46px 0 22px;
  }
  .licences { font-size: 24px; font-weight: 400; letter-spacing: .5px; }

  /* Back */
  .card--back {
    background: radial-gradient(circle at 55% 35%, var(--paper) 0%, var(--paper-shade) 100%);
    display: flex;
    align-items: center;
    padding: 0 48px 0 52px;
  }
  .card--back .brand {
    flex: none;
    width: 400px;
    font-size: 25px;
    color: var(--brand-blue);
    gap: 12px;
    padding-top: 80px;
  }
  .card--back .brand__dot { width: 22px; height: 22px; background: var(--sky); }
  .contact { color: var(--ink); white-space: nowrap; }
  .contact__name { font-size: 38px; font-weight: 800; color: var(--navy); line-height: 1.1; }
  .contact__role { font-size: 17px; margin-top: 2px; }
  .contact__rule { width: 24px; height: 2px; background: var(--ink); margin: 16px 0 10px; }
  .contact__list { list-style: none; font-size: 17px; line-height: 1.65; }
  .contact__list li { display: flex; }
  .contact__label { font-weight: 600; width: 40px; flex: none; }
</style>
</head>
<body>
  <section class="card card--front" aria-label="Card front">
    <div class="brand"><span class="brand__dot"></span>Harbourline Refrigeration</div>
    <div class="licence-rule"></div>
    <p class="licences">AU61420, BLD472913</p>
  </section>

  <section class="card card--back" aria-label="Card back">
    <div class="brand"><span class="brand__dot"></span>Harbourline Refrigeration</div>
    <div class="contact">
      <h1 class="contact__name">Daniel Whitford</h1>
      <p class="contact__role">Founder &amp; CEO</p>
      <div class="contact__rule"></div>
      <ul class="contact__list">
        <li><span class="contact__label">T:</span>(08) 8721 5940</li>
        <li><span class="contact__label">E:</span>harbourserve@tealnet.example</li>
        <li><span class="contact__label">W:</span>www.harbourlinerefrigeration.example</li>
      </ul>
      <div class="contact__rule"></div>
      <ul class="contact__list">
        <li><span class="contact__label">A:</span><span>Shed 5/284 Tallis Rd, Carrick Vale<br>Brennan SA 5790</span></li>
      </ul>
    </div>
  </section>
</body>
</html>
```